Newlyweds banner image for wedding reception

Banner with the words “Just Married” (No quotations) in an elegant and thick (bold) font. Font must be easy to read. Gold or silver letters. Words should easily be edited so that we have the option to print in gold or silver. No background. Image must have source file as well as be delivered as a png with a transparent background. Image will be printed in a horizontal orientation. Must be 300 Dpi for printing. Image must not lose any quality and remain crisp and sharp when expanded and printed to a size of up to 6 feet wide and 2 feet tall. Be creative but we are looking for an elegant option. First and foremost.

Target Market(s)

Wedding planners, brides planning wedding and reception

Industry/Entity Type

Wedding decoration

Colors

Designer to choose colors to be used in the design.

Requirements
Must have
• Gold or Silver letters
Should not have
• Do not mix colors

```html
<!DOCTYPE html>
<html lang="en">
<head>
<meta charset="utf-8">
<title>Just Married — Reception Banner</title>
<link href="https://fonts.googleapis.com/css2?family=Cinzel:wght@700&display=swap" rel="stylesheet">
<style>
  :root {
    --page-bg: #fdfdf9;
    --banner-dark: #000000;
    --banner-mid: #1c1c1c;
    --gold: #d9bb5c;
    --gold-line: #c9a443;
    --ornament-soft: rgba(201, 164, 67, 0.55);
  }
  html, body {
    margin: 0;
    padding: 0;
    width: 910px;
    height: 1200px;
    overflow: hidden;
    background: var(--page-bg);
  }
  .canvas {
    position: relative;
    width: 910px;
    height: 1200px;
  }
  .banner {
    position: absolute;
    left: 45px;
    top: 463px;
    width: 820px;
    height: 274px;
    background: radial-gradient(ellipse 60% 70% at 50% 45%, var(--banner-mid) 0%, var(--banner-dark) 100%);
    box-shadow: 0 10px 28px rgba(0, 0, 0, 0.28);
  }
  .banner-frame {
    position: absolute;
    inset: 0;
  }
  .ornament {
    position: absolute;
    top: 80px;
    width: 34px;
    height: 115px;
    border-radius: 17px;
    background: radial-gradient(ellipse at center, var(--ornament-soft) 0%, rgba(201, 164, 67, 0.15) 60%, transparent 100%);
  }
  .ornament-left { left: 18px; }
  .ornament-right { left: 765px; }
  .banner-title {
    position: absolute;
    left: 0;
    right: 0;
    top: 98px;
    margin: 0;
    text-align: center;
    font-family: 'Cinzel', 'Trajan Pro', serif;
    font-weight: 700;
    font-size: 74px;
    line-height: 80px;
    letter-spacing: 2px;
    color: var(--gold);
    white-space: nowrap;
  }
</style>
</head>
<body>
  <div class="canvas">
    <section class="banner">
      <svg class="banner-frame" width="820" height="274" viewBox="0 0 820 274" aria-hidden="true">
        <path d="M89 49 H728 A34 34 0 0 0 762 83 V190 A34 34 0 0 0 728 224 H89 A34 34 0 0 0 55 190 V83 A34 34 0 0 0 89 49 Z"
              fill="none" stroke="var(--gold-line)" stroke-width="2.5"/>
      </svg>
      <div class="ornament ornament-left" role="img" aria-label="Gold filigree flourish ornament"></div>
      <div class="ornament ornament-right" role="img" aria-label="Gold filigree flourish ornament"></div>
      <h1 class="banner-title">JUST MARRIED</h1>
    </section>
  </div>
</body>
</html>
```